Social Media Marketing website

Need website designed for social media marketing company BrightLoop.com
Do no currently have logo.
Pages:
Main
Services
Order
Contact
Please use dummy text for now. I will provide content to winner later to add.
Main page should clearly show the steps with some sort of graphic: Establish, Engage, Analyze.
Services provided (steps):
1) Establish social media presence
2) Social media management and advertising
3) Analyze and engage
Site should be simple, clean and attractive. Design examples:
http://plinkster.com/
http://www.quillbase.com/
http://www.harrowvalemq.com/
Be creative! It should not look like a template.
Updates
Updated examples.
Contact me for questions.
dave@brightloop.com
3) Analyze and engage
Advertising

```html
<!DOCTYPE html>
<html lang="en">
<head>
<meta charset="utf-8">
<title>BrightLoop — Social Media Marketing</title>
<link rel="stylesheet" href="https://fonts.googleapis.com/css2?family=Arimo:wght@400;700&display=swap">
<style>
:root{
  --teal:#64b6cc;
  --teal-dark:#4fa3ba;
  --ink:#111;
  --body:#555;
  --muted:#888;
  --line:#d6d6d6;
  --paper:#fff;
  --mist:#f3f3f3;
}
*{box-sizing:border-box;margin:0;padding:0}
html,body{width:1200px;height:1147px;overflow:hidden}
body{position:relative;font-family:"Arimo",Arial,sans-serif;color:var(--body);
  background:linear-gradient(#fff 0,#fff 354px,#d9d9d9 430px,#f7f7f7 470px,#fbfbfb 820px,#eeeeee 1032px)}
.abs{position:absolute}
.brand{display:flex;align-items:center;gap:12px;font-weight:700;font-size:30px;color:var(--teal);letter-spacing:.5px}
.brand-mark{width:26px;height:26px;background:var(--teal);border-radius:5px}
.site-header .brand{left:60px;top:68px}
.main-nav{top:91px;left:557px;width:600px;height:20px}
.main-nav a{position:absolute;font-size:14px;font-weight:700;color:var(--teal);text-decoration:none;letter-spacing:.3px}
.main-nav a.current{color:var(--ink)}
.intro{left:69px;top:226px;width:620px;font-size:13px;line-height:21px}
.intro p+p{margin-top:21px}
.btn{left:498px;top:344px;width:178px;height:49px;background:var(--teal);color:#fff;font-size:17px;
  display:flex;align-items:center;justify-content:center;text-decoration:none;letter-spacing:.3px}
.hero-art{left:800px;top:263px;width:333px;height:167px;border-radius:40px 40px 10px 10px;
  background:radial-gradient(ellipse at 50% 30%,#f5c14a 0,#e65a3b 35%,#4fa8d8 65%,rgba(255,255,255,0) 80%)}
.step{width:360px}
.step-art{width:150px;height:146px;border-radius:6px;background:linear-gradient(135deg,#e4edf3,#b7d3e4)}
.step h2{position:absolute;font-size:20px;font-weight:700;color:var(--ink);letter-spacing:.5px}
.step .rule{position:absolute;height:6px;background:var(--teal)}
.step p{position:absolute;font-size:13px;line-height:21px;color:var(--body)}
.step .more{position:absolute;font-size:13px;font-weight:700;color:var(--ink);text-decoration:underline}
.contact-box{left:53px;top:850px;width:1093px;height:132px;border:2px solid #cfcfcf;border-radius:10px;
  background:linear-gradient(#fff,#f1f1f1);box-shadow:0 3px 6px rgba(0,0,0,.25)}
.contact-box h2{position:absolute;left:10px;top:20px;font-size:20px;font-weight:700;color:var(--ink)}
.divider{position:absolute;top:20px;width:2px;height:90px;background:var(--line)}
.contact-item{position:absolute;font-size:14px;color:#333;line-height:22px}
.contact-item strong{display:block;color:var(--ink);font-size:15px}
.social{position:absolute;width:36px;height:36px;border-radius:50%;box-shadow:0 2px 3px rgba(0,0,0,.3)}
.site-footer{left:0;top:1032px;width:1200px;height:115px;background:var(--teal)}
.footer-links{position:absolute;left:61px;top:36px;font-size:13px;color:#fff}
.footer-links a{color:#fff;text-decoration:none}
.copyright{position:absolute;left:61px;top:59px;font-size:12px;color:#eaf6fa}
.site-footer .brand{position:absolute;left:907px;top:28px;color:#1e6f86}
.site-footer .brand-mark{background:#1e6f86}
</style>
</head>
<body>
<header class="site-header">
  <div class="brand abs"><span class="brand-mark"></span>BrightLoop</div>
  <nav class="main-nav abs">
    <a class="current" href="#" style="left:0">MAIN</a>
    <a href="#" style="left:107px">SERVICES</a>
    <a href="#" style="left:249px">PORTFOLIO</a>
    <a href="#" style="left:400px">ORDER</a>
    <a href="#" style="left:522px">CONTACT</a>
  </nav>
</header>

<section class="hero">
  <div class="intro abs">
    <p>Not only do your current and future customers expect your business to have a professional, engaging social media presence, but social media outlets could be the least expensive and most effective marketing tools at your disposal.</p>
    <p>BrightLoop will help your business establish and enhance your social media presence, engage your customers, and analyze results.</p>
  </div>
  <a class="btn abs" href="#">LEARN MORE →</a>
  <div class="hero-art abs" role="img" aria-label="Group of colourful figures with speech bubbles of social networks"></div>
</section>

<section class="steps">
  <div class="step abs" style="left:40px;top:506px">
    <div class="step-art" role="img" aria-label="Tablet in front of a globe"></div>
    <h2 style="left:166px;top:68px">ESTABLISH</h2>
    <div class="rule" style="left:17px;top:145px;width:318px"></div>
    <p style="left:17px;top:170px;width:340px">We create a professional Friendbase fan page for you and help you build your brand on Chirper, Clipstream, your blog and much more.</p>
    <a class="more" href="#" style="left:247px;top:253px">LEARN MORE</a>
  </div>
  <div class="step abs" style="left:420px;top:506px">
    <div class="step-art" role="img" aria-label="Two glossy speech bubbles"></div>
    <h2 style="left:143px;top:64px">PROMOTE</h2>
    <div class="rule" style="left:21px;top:145px;width:322px"></div>
    <p style="left:21px;top:170px;width:340px">Attract fans/followers, advertise, SEO optimization, cross integration of content, polls, contests, coupons and much more.</p>
    <a class="more" href="#" style="left:253px;top:253px">LEARN MORE</a>
  </div>
  <div class="step abs" style="left:808px;top:506px">
    <div class="step-art" role="img" aria-label="Magnifying glass over report papers"></div>
    <h2 style="left:153px;top:62px">ANALYZE</h2>
    <div class="rule" style="left:18px;top:145px;width:322px"></div>
    <p style="left:18px;top:170px;width:340px">Monitor, analyze and engage your brand and customers with our powerful social media tool.</p>
    <a class="more" href="#" style="left:245px;top:253px">LEARN MORE</a>
  </div>
</section>

<section class="contact-box abs">
  <h2>GET IN TOUCH</h2>
  <svg class="abs" style="left:100px;top:40px" width="44" height="52" viewBox="0 0 44 52" aria-hidden="true">
    <g transform="rotate(-25 22 26)"><rect x="12" y="4" width="20" height="42" rx="4" fill="#666"/><rect x="15" y="9" width="14" height="14" fill="#cfe3ea"/><g fill="#ddd"><circle cx="18" cy="29" r="1.6"/><circle cx="22" cy="29" r="1.6"/><circle cx="26" cy="29" r="1.6"/><circle cx="18" cy="34" r="1.6"/><circle cx="22" cy="34" r="1.6"/><circle cx="26" cy="34" r="1.6"/><circle cx="18" cy="39" r="1.6"/><circle cx="22" cy="39" r="1.6"/><circle cx="26" cy="39" r="1.6"/></g></g>
  </svg>
  <div class="contact-item" style="left:166px;top:44px"><strong>Phone</strong>(866) 555-0142</div>
  <div class="divider" style="left:346px"></div>
  <svg class="abs" style="left:436px;top:42px" width="50" height="50" viewBox="0 0 50 50" aria-hidden="true">
    <rect x="4" y="6" width="42" height="40" rx="3" fill="#f2a93b"/><rect x="4" y="6" width="42" height="40" rx="3" fill="none" stroke="#c77e1c" stroke-width="2"/><path d="M6 10 L25 28 L44 10" fill="none" stroke="#fff" stroke-width="3"/>
  </svg>
  <div class="contact-item" style="left:510px;top:44px"><strong>Email Address</strong>sales@brightloop.com</div>
  <div class="divider" style="left:742px"></div>
  <span class="social" style="left:812px;top:48px;background:#3ab3e0"></span>
  <span class="social" style="left:864px;top:48px;background:#3b5998"></span>
  <span class="social" style="left:917px;top:48px;background:#e8e8ee"></span>
  <span class="social" style="left:971px;top:48px;background:#f07a1a"></span>
</section>

<footer class="site-footer abs">
  <div class="footer-links"><a href="#">Main</a> &nbsp;|&nbsp; <a href="#">Services</a> &nbsp;|&nbsp; <a href="#">Portfolio</a> &nbsp;|&nbsp; <a href="#">Order</a> &nbsp;|&nbsp; <a href="#">Contact</a></div>
  <div class="copyright">© 2011 BrightLoop. All Rights Reserved.</div>
  <div class="brand"><span class="brand-mark"></span>BrightLoop</div>
</footer>
</body>
</html>
```